Early Learning & Child Care A5 Flyer – Enrolment Awareness Campaign

• A5 Flyer Sketch Meadow Brief
o Document: A5 Flyer Portrait.
 Height = 210mm
 Width = 148mm
o Pages: 2 (Double sided)
o Colour: In keeping with our logo (refer attached PDF)
o Content: Front page (refer attached pdf)
o Content: Back page (refer attached pdf)
o Fonts: Headings: Aclonica, Text: Baloo 2
o Logo:
 EPS & PDF (refer attached, other file options available upon request)
 White & Translucent background (refer attached)
 Placement: Front & Back pages
o Photo Front Page:
 Creek Bed – This is the main photo but don’t make it too large as it will reduce the image quality
 Collecting Eggs – FACE TOO BE BLURRED, smaller in size than mani photo
o Photo Back Page:
 Mud Day Hands
 Outdoor Activity
 Toddlers Sleeping
o Website QR code: Placement front and back pages next to contact details
o Finished A5 flyer to provide in PDF format and PDF format with 10mm bleed on all four sides (230mm x 168mm)
o Files to be provided
 PDF without bleed
 PDF with bleed
 EPS with bleed
 EPS without bleed
o Fonts – Name of fonts used required
o Colours – names of colours used in HEX, CMYK/Pantone and RBG

Refer attached PDF and associated files as mentioned in the A5 Flyer SketchMeadow Brief

Target Market(s)

Families looking for Child Care

Industry/Entity Type

Child Care

Requirements
Must have
• Refer attached A5 Flyer SketchMeadow Brief
Nice to have

```html
<!DOCTYPE html>
<html lang="en">
<head>
<meta charset="utf-8">
<title>Wattle Sprouts – A5 Enrolment Flyer</title>
<link rel="stylesheet" href="https://fonts.googleapis.com/css2?family=Montserrat:wght@400;500;600;700&display=swap">
<style>
:root{
  --brown:#8a5320;
  --yellow:#f7b719;
  --green:#5f9b32;
  --green-bright:#6aaa2e;
  --ink:#1e1e1e;
  --white:#ffffff;
  --stage:#e7e7e7;
  --photo-warm:#b08a6a;
  --photo-earth:#8e7a5c;
}
*{margin:0;padding:0;box-sizing:border-box}
html,body{width:892px;height:1200px;overflow:hidden}
body{background:var(--stage);font-family:"Montserrat",Arial,sans-serif;color:var(--ink);position:relative}
.page{position:absolute;top:290px;width:436px;height:619px;background:var(--white);overflow:hidden;box-shadow:0 2px 6px rgba(0,0,0,.18)}
.page--front{left:7px}
.page--back{left:449px}
.art{position:absolute;left:0;top:0}

/* front */
.side-panel{position:absolute;left:0;top:172px;width:161px;height:447px;background:var(--brown);padding:20px 12px 0 19px;color:var(--white)}
.enrol-title{color:var(--yellow);font-weight:700;font-size:13.2px;line-height:1.2;margin-bottom:9px}
.tagline{color:var(--green-bright);font-weight:700;font-size:10.6px;line-height:1.2;margin-bottom:10px}
.side-panel p{font-size:8.6px;line-height:1.27;margin-bottom:10px}
.brand{position:absolute;left:128px;top:40px;display:flex;align-items:center;gap:5px}
.brand-dot{width:22px;height:22px;border-radius:50%;background:var(--green)}
.brand-name{font-weight:700;font-size:15px;color:var(--green);white-space:nowrap}
.features{position:absolute;left:179px;top:300px;width:250px}
.section-title{color:var(--green-bright);font-weight:700;font-size:9.8px;margin-bottom:3px}
.section-sub{color:var(--green-bright);font-weight:700;font-size:8.4px;margin:-3px 0 3px}
.bullets{list-style:none;font-size:8.1px;line-height:1.22;margin-bottom:11px}
.bullets li{padding-left:8px;text-indent:-5px;margin-bottom:2.6px}
.bullets li::before{content:"•";margin-right:3px}

/* back */
.back-intro{position:absolute;left:17px;top:166px;width:405px}
.back-title{color:var(--green-bright);font-weight:700;font-size:14.5px;line-height:1.2;margin-bottom:8px}
.back-intro p{font-size:8.9px;line-height:1.25}
.col{position:absolute;top:266px}
.col--left{left:28px;width:140px}
.col--right{left:212px;width:212px;top:287px}
.special-title{color:var(--brown);font-weight:700;font-size:11px;line-height:1.2;margin-bottom:10px}
.item-title{color:var(--green-bright);font-weight:700;font-size:8.9px;margin-bottom:4px}
.item-text{font-size:8.9px;line-height:1.2;margin-bottom:11px}
.cta{position:absolute;left:12px;top:544px;width:120px;color:var(--white);font-size:8.4px;line-height:1.22}
.cta-phone{display:block;color:var(--yellow);font-weight:700;font-size:11.5px;margin-top:9px}
.contact{position:absolute;left:170px;top:574px;width:266px;height:45px;background:var(--green);color:var(--white);font-size:7.2px;font-weight:500;line-height:1.35;text-align:center;padding-top:5px}
</style>
</head>
<body>

<section class="page page--front" aria-label="Flyer front">
  <svg class="art" width="436" height="292" viewBox="0 0 436 292">
    <rect x="0" y="0" width="230" height="190" fill="#a496a6" role="img" aria-label="Photo of a child holding freshly collected eggs"/>
    <rect x="165" y="196" width="133" height="96" fill="var(--photo-earth)" role="img" aria-label="Photo of a child climbing logs in the playground"/>
    <rect x="300" y="196" width="136" height="96" fill="var(--photo-warm)" role="img" aria-label="Photo of sandy hands on mud day"/>
    <path d="M0 150 Q95 190 200 166 L200 176 Q95 200 0 174 Z" fill="var(--yellow)"/>
    <circle cx="350" cy="-10" r="205" fill="var(--white)"/>
    <circle cx="350" cy="-10" r="200" fill="none" stroke="var(--green)" stroke-width="3"/>
    <circle cx="350" cy="-10" r="196" fill="#6f7552" role="img" aria-label="Photo of children exploring the creek bed with an educator"/>
    <rect x="0" y="0" width="120" height="0" fill="none"/>
  </svg>
  <div class="brand"><span class="brand-dot"></span><span class="brand-name">Wattle Sprouts</span></div>

  <div class="side-panel">
    <h1 class="enrol-title">ENROL NOW AT WATTLE SPROUTS</h1>
    <p class="tagline">Growing curious, confident children—naturally.</p>
    <p>Since 2014, Wattle Sprouts has been a place where children feel safe, supported and inspired to be themselves. As a privately family-owned childcare centre, we welcome babies through to preschoolers (0–6 years) into a warm, caring environment where learning happens naturally—through play, connection and discovery.</p>
    <p>Every day at Wattle Sprouts is an adventure. Children explore thoughtfully designed outdoor spaces that encourage curiosity, resilience and wonder.</p>
  </div>

  <div class="features">
    <h2 class="section-title">What Sets Us Apart</h2>
    <ul class="bullets">
      <li>Two large nature playgrounds spanning over 560m²</li>
      <li>Natural, eco-friendly surfaces (no fake grass)</li>
      <li>30+ mature Australian native trees</li>
      <li>Mud kitchens and sand pits for sensory play</li>
      <li>Creek bed adventures and an outdoor fire pit</li>
      <li>The option to sleep outdoors (introduced in 2017 for children aged 2 and above – not babies)</li>
      <li>Animal husbandry: feeding our heritage chickens and collecting fresh eggs</li>
      <li>Gardening and composting for sustainability</li>
      <li>Nature-based STEAM experiences</li>
    </ul>
    <h2 class="section-title">Why Nature Matters</h2>
    <p class="section-sub">Research shows time in nature supports:</p>
    <ul class="bullets">
      <li>Emotional wellbeing – calming natural spaces that reduce stress and boost happiness</li>
      <li>Physical development – climbing and exploring builds strength and coordination</li>
      <li>Cognitive growth – hands-on play encourages problem-solving and creativity</li>
      <li>Environmental responsibility – children learn respect and responsibility through real experiences</li>
    </ul>
  </div>
</section>

<section class="page page--back" aria-label="Flyer back">
  <svg class="art" width="436" height="619" viewBox="0 0 436 619">
    <path d="M16 0 Q32 118 140 170 Q260 222 436 196" fill="none" stroke="var(--green)" stroke-width="3"/>
    <path d="M24 0 H436 V190 Q262 214 146 162 Q42 112 24 0 Z" fill="#7a2a2a" role="img" aria-label="Photo of toddlers resting on mats outdoors"/>
    <path d="M0 516 Q140 506 186 619 L0 619 Z" fill="var(--yellow)"/>
    <path d="M0 524 Q128 518 172 619 L0 619 Z" fill="var(--brown)"/>
  </svg>

  <div class="back-intro">
    <h2 class="back-title">Why Families<br>Choose Wattle Sprouts</h2>
    <p>Choosing care for your child is one of the most important decisions you’ll make. At Wattle Sprouts, we partner with families to create a loving, inclusive and inspiring place where your child can truly thrive.</p>
  </div>

  <div class="col col--left">
    <h3 class="special-title">Here’s what makes us special:</h3>
    <h4 class="item-title">Engaging Daily Activities</h4>
    <p class="item-text">Creative, inspiring experiences that foster independence, confidence and strong social skills.</p>
    <h4 class="item-title">Outdoor Play &amp; Exploration</h4>
    <p class="item-text">A strong emphasis on outdoor learning, nature play and sustainable practices – every single day.</p>
    <h4 class="item-title">Nutritious Meals</h4>
    <p class="item-text">Our in-house chef prepares fresh, healthy meals daily to nourish growing bodies and minds.</p>
  </div>

  <div class="col col--right">
    <h4 class="item-title">Caring Educators</h4>
    <p class="item-text">Qualified, experienced educators commited to your child’s development in a safe and supportive environment.</p>
    <h4 class="item-title">Unique Curriculum</h4>
    <p class="item-text">Inspired by the Reggio Emilia approach, our play-based curriculum values each child’s individuality and encourages learning through exploration and creativity.</p>
    <h4 class="item-title">Inclusive &amp; Diverse Community</h4>
    <p class="item-text">We celebrate diversity and embrace every child’s unique strengths and learning style.</p>
    <h4 class="item-title">Mobile-Free Environment</h4>
    <p class="item-text">Our educators are fully present, giving children the attention, care and connection they deserve.</p>
    <p class="item-text">We also offer extensive activities through our broad enrichment program to keep children engaged, curious and learning.</p>
  </div>

  <p class="cta">3 Day Child Care Guarantee Available NOW - Book a tour or call us today<span class="cta-phone">9200 4187</span></p>
  <div class="contact">118 – 120 Banksia Road, Red Hill Grove<br>Monday – Friday, 6:30am – 5:30pm<br>hello@wattlesprouts.edu.au &nbsp;|&nbsp; www.wattlesprouts.edu.au</div>
</section>

</body>
</html>
```